Graphic Design for a Info Card

We would like a graphic design for an info card . We would like the colours to correspond to our logo , you can add in the colours navy blue or yellow if you would like. We would like it to have the following information. We want something that really pops. We would like the size to be 4 1/2 x 6 .

ATTENTION!! Delivery Promo! Order from us on the @hopplemeals app or @marlinrunner app on FRIDAYS and receive a FREE Sample of our one of our meal prep meals in your bag!
DID YOU KNOW?! Meal Prep is another great service that we offer. Saving you time, promoting your health, and best of all providing a delicious lunch . You can find more info on our website www.brivoranpantry.example . All orders are available for delivery or pickup!

```html
<!DOCTYPE html>
<html lang="en">
<head>
<meta charset="utf-8">
<title>Brivoran Delivery Promo Info Card</title>
<link href="https://fonts.googleapis.com/css2?family=Bitter:wght@300;400;700;900&family=Roboto:wght@300;700;900&display=swap" rel="stylesheet">
<style>
  :root {
    --page-bg: #e9e6e1;
    --brand-green: #8cc63f;
    --brand-green-deep: #6fa82a;
    --promo-cream: #eef6dc;
    --promo-ink: #3b4a24;
    --body-grey: #8b8b8b;
    --body-grey-dark: #6d6d6d;
    --side-grey: #c9c9c9;
    --paper: #ffffff;
  }
  * { box-sizing: border-box; margin: 0; padding: 0; }
  html, body { width: 1200px; height: 1200px; overflow: hidden; background: var(--page-bg); }

  .info-card {
    position: absolute; left: 180px; top: 40px;
    width: 840px; height: 1120px;
    background: var(--paper);
    overflow: hidden;
    box-shadow: 0 6px 24px rgba(0,0,0,.18);
  }

  .photo-top {
    position: absolute; left: 0; top: 0; width: 100%; height: 175px;
    background: linear-gradient(90deg, #d8b48e 0%, #9a3b4a 38%, #6e1f30 58%, #4f8a2c 80%, #3d7325 100%);
  }
  .photo-dishes {
    position: absolute; left: 0; top: 380px; width: 100%; height: 430px;
    background:
      linear-gradient(180deg, rgba(255,255,255,0) 45%, #ffffff 100%),
      linear-gradient(90deg, #c9a273 0%, #d9b98e 38%, #b9bcbb 60%, #a9adad 100%);
  }

  .promo-band {
    position: absolute; left: 0; top: 160px; width: 100%; height: 245px;
    background: var(--brand-green);
  }
  .promo-title {
    position: absolute; left: 70px; top: 8px;
    font-family: "Bitter", serif; font-weight: 900;
    font-size: 88px; line-height: 1; color: #fff; letter-spacing: 1px;
  }
  .promo-subtitle {
    position: absolute; left: 72px; top: 108px;
    font-family: "Bitter", serif; font-weight: 300;
    font-size: 62px; line-height: 66px; color: var(--promo-cream);
  }
  .promo-details {
    position: absolute; left: 360px; top: 112px; width: 400px;
    font-family: "Bitter", serif; font-weight: 300;
    font-size: 17px; line-height: 27px; color: var(--promo-ink); text-align: center;
  }
  .promo-details strong { font-weight: 700; }

  .side-strip { position: absolute; top: 790px; bottom: 0; width: 30px; background: var(--side-grey); }
  .side-strip--left { left: 0; }
  .side-strip--right { right: 0; }

  .about {
    position: absolute; left: 80px; top: 800px; width: 700px;
  }
  .about-heading {
    font-family: "Bitter", serif; font-weight: 900;
    font-size: 44px; line-height: 1; color: var(--brand-green);
  }
  .about-body {
    margin-top: 8px;
    font-family: "Bitter", serif; font-weight: 400;
    font-size: 29px; line-height: 38px; color: var(--body-grey);
  }
  .about-body strong { font-weight: 700; color: var(--body-grey-dark); }

  .social-links { position: absolute; right: 80px; top: 930px; display: flex; gap: 14px; }
  .social-dot { width: 50px; height: 50px; border-radius: 50%; background: #cfd3d6; }

  .contact {
    position: absolute; left: 80px; top: 990px; width: 400px;
    font-family: "Roboto", sans-serif; font-weight: 300;
    font-size: 21px; line-height: 30px; color: var(--brand-green);
  }
  .contact strong { font-weight: 900; font-size: 22px; }

  .brand-mark { position: absolute; right: 64px; top: 1005px; text-align: right; }
  .brand-name {
    display: flex; align-items: center; justify-content: flex-end; gap: 10px;
    font-family: "Roboto", sans-serif; font-weight: 900;
    font-size: 54px; line-height: 1; color: var(--brand-green); letter-spacing: 2px;
  }
  .brand-name::before {
    content: ""; width: 14px; height: 14px; border-radius: 50%; background: var(--brand-green);
  }
  .brand-tagline {
    margin-top: 6px;
    font-family: "Roboto", sans-serif; font-weight: 700;
    font-size: 19px; color: var(--brand-green); letter-spacing: .5px;
  }
</style>
</head>
<body>
  <main class="info-card">
    <div class="photo-top" role="img" aria-label="Overhead photo of fresh salads with beets, spinach and grilled chicken"></div>
    <div class="photo-dishes" role="img" aria-label="Photo of a creamy chicken and vegetable bowl, grilled zucchini and sweet potatoes, and two forks on a linen napkin"></div>

    <section class="promo-band">
      <h1 class="promo-title">ATTENTION!!</h1>
      <p class="promo-subtitle">Delivery<br>Promo!</p>
      <p class="promo-details">Order from us on the <strong>@hopplemeals</strong> app or <strong>@marlinrunner</strong> app on FRIDAYS and receive a <strong>FREE Sample</strong> of our one of our meal prep meals in your bag!</p>
    </section>

    <div class="side-strip side-strip--left"></div>
    <div class="side-strip side-strip--right"></div>

    <section class="about">
      <h2 class="about-heading">DID YOU KNOW?!</h2>
      <p class="about-body"><strong>Meal Prep</strong> is another great service that we offer. Saving you time, promoting your health, and best of all providing a <em>delicious</em> lunch.</p>
    </section>

    <div class="social-links">
      <span class="social-dot" aria-label="Photo sharing profile"></span>
      <span class="social-dot" aria-label="Social network profile"></span>
    </div>

    <p class="contact">You can find more info on our website <strong>www.brivoranpantry.example.</strong><br>All orders are available for delivery or pickup!</p>

    <div class="brand-mark">
      <div class="brand-name">BRIVORAN</div>
      <div class="brand-tagline">HEALTHY KITCHEN | MEAL PREP</div>
    </div>
  </main>
</body>
</html>
```